Australian Online Training Organisation needs a Website Design

We need a Web Design ideally using a Wordpress Divi template which will represent an Australian Online Training Company.

(Harlow Net Learning)

The website will represent a range of short courses with an emphasis on business, zentrosoft, leadership etc.

The website will 'shell out' to the third party portal where 'bookings' occur. I am imaging a fantastic looking web design with perhaps 5-6 pages.

I am wondering if a selection of courses including the below list can be incorporated?

The variety of courses include :

Workplace Safety
Sales Training
Leadership
Process Management
Problem Solving
Project Management
Business Planning
Meetings and Events
Emotional Intelligence
Human Resources
Administrative Essentials
Customer Service
Career Development
Conflict Resolution
Train the Trainer
Supervisors and Managers
Internet marketing
Communications
Team Building
Marketing
Finance
Writing
Job Search Skills
Public Speaking
Negotiation Skills
Talent Management
Zentrosoft Deskline 2016
ZDC Preparation for Office 2010
Office 2013
Office 2010
Upgrading to Office 2010
Computer Fundamentals
Upgrading to Office 2007
Office 2003
Office 2002
Pavra Suite X3
Core Essentials
Office 2007

Thank you so much for all of the amazing designs we received. We were so happy with so many elements that it was very hard to choose. Our top two were very hard to decide upon but we look forward to working more with both of these talents into the future. Thank you again.

Target Market(s)

Professionals, students and workers who would like to improve their skills with online training in over 500 + courses -

Industry/Entity Type

It Company

Number of Pages Required

5+ page

Font styles to use
Sans Serif

Colors
3276b5
faa54b
0355a3
fac994

Requirements
Must have
• Ideally would use Wordpress theme (Divi for example or other)
• Very smart front end
• Will upload logo soon
• (Harlow Net Learning)
• harlownetlearning.edu.au
• Graphics of 'people' pretty important - with a variety of ages.
Nice to have
• Interesting page
• National presence
• A bit University looking
• Professional
• Graphics of people
• Blog
• Graphics of people
• Age range from job seekers, to business folk, etc

```html
<!DOCTYPE html>
<html lang="en">
<head>
<meta charset="utf-8">
<title>Harlow Net Learning — Online Training Company</title>
<link rel="stylesheet" href="https://fonts.googleapis.com/css2?family=Libre+Baskerville&family=Montserrat:wght@300;400;500&display=swap">
<style>
:root{
  --navy:#253f63;
  --navy-text:#2c4a6e;
  --orange:#f39320;
  --orange-soft:#fac994;
  --grey-band:#efefef;
  --footer:#2a2a2a;
  --text:#3a3a3a;
  --muted:#8a8a8a;
  --white:#ffffff;
  --serif:"Libre Baskerville",Georgia,serif;
  --sans:"Montserrat",Arial,sans-serif;
}
*{box-sizing:border-box;margin:0;padding:0}
html,body{width:1200px;height:3243px;overflow:hidden}
body{position:relative;font-family:var(--sans);color:var(--text);background:var(--white)}
.abs{position:absolute}
.center{left:0;width:1200px;text-align:center}

/* header */
.site-header{top:0;left:0;width:1200px;height:70px;background:var(--white)}
.brand{left:108px;top:22px;display:flex;align-items:center;gap:10px;font-family:var(--serif);font-size:16px;color:var(--navy);white-space:nowrap}
.brand-mark{width:20px;height:24px;background:var(--navy)}
.main-nav{left:352px;top:29px;width:744px;display:flex;justify-content:space-between;font-family:var(--serif);font-size:10.5px;color:#6b6b6b;white-space:nowrap}
.main-nav .active{color:var(--navy)}

/* hero */
.hero{top:70px;left:0;width:1200px;height:530px;background:linear-gradient(160deg,#5a4a3e 0%,#3a3530 45%,#2a2c30 100%)}
.hero-shade{top:70px;left:0;width:1200px;height:530px;background:rgba(20,20,24,.35)}
.hero-title{top:218px;font-family:var(--serif);font-size:38px;color:var(--white);letter-spacing:1px}
.hero-sub{top:284px;font-size:15px;color:var(--white)}
.hero-sub em{font-style:normal;color:var(--orange)}
.hero-sub .gap{display:inline-block;width:52px}
.search{left:216px;top:348px;width:768px;height:43px;background:var(--white);display:flex}
.search-field{flex:1;padding:14px 18px;font-size:13px;color:#999}
.search-btn{width:50px;height:43px;background:var(--orange);display:flex;align-items:center;justify-content:center}
.hero-note{left:216px;top:400px;width:768px;text-align:center;font-size:13px;line-height:20px;color:#e6e6e6}
.chat{left:980px;top:143px;width:220px;height:75px;background:var(--white);display:flex;align-items:center}
.chat-photo{width:58px;height:75px;background:linear-gradient(180deg,#e9dccf,#c7b7a8)}
.chat-close{left:0;top:0;width:18px;height:18px;background:var(--navy)}
.chat-text{margin-left:14px;font-family:var(--serif);font-size:17px;line-height:23px;color:var(--navy)}
.chat-text span{color:var(--orange)}

/* trusted */
.trusted{top:600px;left:0;width:1200px;height:399px;background:var(--navy)}
.trusted-title{top:680px;font-family:var(--serif);font-size:23px;color:var(--white);letter-spacing:1px}
.trusted-by{top:727px;font-size:15px;color:var(--white);letter-spacing:1px}
.partners{left:110px;top:788px;width:980px;display:flex;justify-content:space-between;align-items:center;font-family:var(--sans);font-weight:500;font-size:20px;color:var(--white)}
.arrow-l{left:72px;top:790px}
.arrow-r{left:1110px;top:790px}

/* welcome */
.welcome-photo{left:102px;top:902px;width:488px;height:447px;background:linear-gradient(135deg,#eef1f3 0%,#d9dcdc 55%,#b9bfc2 100%);box-shadow:0 6px 18px rgba(0,0,0,.18)}
.welcome-kicker{left:629px;top:1054px;font-family:var(--serif);font-size:23px;color:#1c1c1c;letter-spacing:1px}
.welcome-name{left:629px;top:1088px;font-family:var(--serif);font-size:25px;color:var(--navy-text);letter-spacing:1px}
.welcome-text{left:629px;top:1132px;width:470px;font-size:15px;line-height:22px;color:var(--muted)}
.btn-outline{border:2px solid var(--orange);color:var(--orange);font-size:14px;display:flex;align-items:center;justify-content:center}
.learn-more{left:629px;top:1237px;width:175px;height:41px}

/* features */
.features{top:1436px;left:0;width:1200px;height:434px;background:var(--grey-band)}
.features-title{top:1516px;font-family:var(--serif);font-size:23px;color:#1c1c1c;letter-spacing:1px}
.features-sub{top:1551px;font-family:var(--serif);font-size:23px;color:var(--navy-text);letter-spacing:1px}
.feature{top:1606px;width:300px;text-align:center}
.feature-icon{height:104px;display:flex;align-items:center;justify-content:center}
.feature-name{margin-top:20px;font-size:17px;color:#222}
.feature-desc{margin-top:6px;font-size:13px;line-height:18px;color:var(--muted);padding:0 26px}

/* courses */
.courses-kicker{top:1950px;font-family:var(--serif);font-size:23px;color:#1c1c1c}
.courses-title{top:1986px;font-family:var(--serif);font-size:23px;color:var(--navy-text);letter-spacing:1px}
.course{width:238px}
.course-photo{height:171px}
.course-name{margin-top:13px;text-align:center;font-size:17px;color:#333}
.tone-safety{background:linear-gradient(135deg,#c8c3a8,#8f9a6e 60%,#5f6b50)}
.tone-sales{background:linear-gradient(135deg,#f2f2f2,#c9ced6 60%,#6f7783)}
.tone-lead{background:linear-gradient(135deg,#d8d2cc,#6b6058 55%,#2c2a2c)}
.tone-process{background:linear-gradient(135deg,#dfe6ee,#9fb3c7 55%,#4d6178)}
.view-all{left:495px;top:2530px;width:210px;height:41px}

/* testimonials */
.testimonials{top:2657px;left:0;width:1200px;height:385px;background:var(--grey-band)}
.testimonials-title{top:2738px;font-family:var(--serif);font-size:23px;color:var(--navy-text);letter-spacing:1px}
.avatar{width:103px;height:103px;border-radius:50%;background:linear-gradient(160deg,#c9b6a3,#7d8a99)}
.person{font-size:13px;color:#333;width:103px;text-align:center}
.quote-head{font-size:18px;color:#222}
.quote-body{font-size:13px;line-height:18px;color:var(--muted);width:360px;margin-top:8px}

/* newsletter */
.newsletter{top:3042px;left:0;width:1200px;height:104px;background:var(--navy)}
.newsletter-title{left:102px;top:3084px;font-family:var(--serif);font-size:19px;color:var(--white);letter-spacing:.5px;white-space:nowrap}
.email{left:571px;top:3074px;width:341px;height:41px;background:var(--white);font-size:12px;color:#888;padding:14px 16px}
.submit{left:917px;top:3074px;width:179px;height:41px;background:var(--orange);color:var(--white);font-size:15px;display:flex;align-items:center;justify-content:center}

/* footer */
.site-footer{top:3146px;left:0;width:1200px;height:97px;background:var(--footer)}
.copyright{left:102px;top:3188px;font-size:12px;color:#9a9a9a}
.socials{left:940px;top:3183px;display:flex;gap:8px}
.socials span{width:22px;height:22px;border-radius:50%;background:#9a9a9a;display:block}
</style>
</head>
<body>

<header class="abs site-header">
  <div class="abs brand"><span class="brand-mark"></span>Harlow Net Learning</div>
  <nav class="abs main-nav">
    <span class="active">HOME</span><span>ABOUT</span><span>COURCES</span><span>EMPLOYERS</span><span>TESTIMONIALS</span><span>SUPPORT AND RESOURCES</span><span>BLOG</span><span>CONTACT US</span>
  </nav>
</header>

<section>
  <div class="abs hero" role="img" aria-label="Hands typing on a laptop at a wooden desk"></div>
  <div class="abs hero-shade"></div>
  <h1 class="abs center hero-title">ONLINE TRAINING COMPANY</h1>
  <p class="abs center hero-sub">Range of <em>Short Courses</em><span class="gap"></span>50,000 <em>Job Seekers</em></p>
  <div class="abs search">
    <div class="search-field">Search from 600+ well priced, accessible short courses</div>
    <div class="search-btn">
      <svg width="18" height="18" viewBox="0 0 18 18"><circle cx="7.5" cy="7.5" r="5.5" fill="none" stroke="#fff" stroke-width="2"/><line x1="11.5" y1="11.5" x2="16" y2="16" stroke="#fff" stroke-width="2.4" stroke-linecap="round"/></svg>
    </div>
  </div>
  <p class="abs hero-note">Lorem ipsum dolor sit amet, consectetur adipisicing elit, sed do eiusmod tempor incididunt ut labore et dolore magna aliqua. Ut enim ad minim veniam.</p>
  <div class="abs chat">
    <div class="chat-photo" role="img" aria-label="Support agent with headset"></div>
    <div class="abs chat-close"><svg width="18" height="18" viewBox="0 0 18 18"><path d="M5 5l8 8M13 5l-8 8" stroke="#fff" stroke-width="2"/></svg></div>
    <div class="chat-text">CHAT<br><span>LIVE NOW !</span></div>
  </div>
</section>

<section>
  <div class="abs trusted"></div>
  <h2 class="abs center trusted-title">YOU'RE IN GREAT COMPANY</h2>
  <p class="abs center trusted-by">TRUSTED BY</p>
  <svg class="abs arrow-l" width="16" height="24" viewBox="0 0 16 24"><path d="M12 3L4 12l8 9" fill="none" stroke="#7d8ea8" stroke-width="2"/></svg>
  <div class="abs partners">
    <span>Trivora</span><span>Kanemoto</span><span>Paylo</span><span>Whitlock Banner &amp; Co</span><span>Vessel Media</span><span>Amberly</span>
  </div>
  <svg class="abs arrow-r" width="16" height="24" viewBox="0 0 16 24"><path d="M4 3l8 9-8 9" fill="none" stroke="#7d8ea8" stroke-width="2"/></svg>
</section>

<section>
  <div class="abs welcome-photo" role="img" aria-label="Young woman working on a laptop in a bright office"></div>
  <h2 class="abs welcome-kicker">WELCOME TO</h2>
  <h3 class="abs welcome-name">HARLOW NET LEARNING</h3>
  <p class="abs welcome-text">Harlow Net Learning is one of Australia's leading provider of flexible and affordable online continuing professional development programs, with over 600 online courses now available.</p>
  <div class="abs btn-outline learn-more">Learn More</div>
</section>

<section>
  <div class="abs features"></div>
  <h2 class="abs center features-title">HELPING PEOPLE</h2>
  <h3 class="abs center features-sub">GROW THEIR CAREERS. EVERY DAY!</h3>

  <div class="abs feature" style="left:122px">
    <div class="feature-icon"><div role="img" aria-label="Icon of an expert teaching at a desk" style="width:80px;height:96px;background:linear-gradient(180deg,#f7c98e,#d8d8d8)"></div></div>
    <div class="feature-name">Learn from the Experts</div>
    <div class="feature-desc">Lorem ipsum dolor sit amet, consectetur adipisicing elit.</div>
  </div>
  <div class="abs feature" style="left:447px">
    <div class="feature-icon">
      <svg width="96" height="96" viewBox="0 0 96 96" fill="none">
        <path d="M8 6v82h84" stroke="#9a9a9a" stroke-width="2"/>
        <path d="M8 20h6M8 36h6M8 52h6M8 68h6M24 88v-6M40 88v-6M56 88v-6M72 88v-6" stroke="#9a9a9a" stroke-width="2"/>
        <path d="M22 74L80 22" stroke="var(--orange)" stroke-width="4"/>
        <path d="M66 20h16v16" stroke="var(--orange)" stroke-width="4"/>
      </svg>
    </div>
    <div class="feature-name">Guaranteed career growth</div>
    <div class="feature-desc">Lorem ipsum dolor sit amet, consectetur adipisicing elit.</div>
  </div>
  <div class="abs feature" style="left:775px">
    <div class="feature-icon">
      <svg width="112" height="88" viewBox="0 0 112 88" fill="none">
        <rect x="2" y="4" width="108" height="78" stroke="#9a9a9a" stroke-width="2"/>
        <rect x="9" y="11" width="94" height="64" stroke="#c4c4c4" stroke-width="1.5"/>
        <path d="M20 28h52M20 40h40M20 52h30" stroke="#9a9a9a" stroke-width="2"/>
        <circle cx="84" cy="56" r="10" stroke="var(--orange)" stroke-width="3"/>
        <path d="M78 65l-4 14 10-5 10 5-4-14" stroke="var(--orange)" stroke-width="3"/>
      </svg>
    </div>
    <div class="feature-name">Accredited curriculum</div>
    <div class="feature-desc">Lorem ipsum dolor sit amet, consectetur adipisicing elit.</div>
  </div>
</section>

<section>
  <h2 class="abs center courses-kicker">OUR</h2>
  <h3 class="abs center courses-title">SHORT TERM COURCES</h3>

  <div class="abs course" style="left:102px;top:2045px"><div class="course-photo tone-safety" role="img" aria-label="Worker in hard hat and safety vest"></div><div class="course-name">Workplace Safety</div></div>
  <div class="abs course" style="left:355px;top:2045px"><div class="course-photo tone-sales" role="img" aria-label="Presenter at a whiteboard in a meeting"></div><div class="course-name">Sales Training</div></div>
  <div class="abs course" style="left:608px;top:2045px"><div class="course-photo tone-lead" role="img" aria-label="Business team standing together"></div><div class="course-name">Leadership</div></div>
  <div class="abs course" style="left:860px;top:2045px"><div class="course-photo tone-process" role="img" aria-label="Colleagues reviewing work at a computer"></div><div class="course-name">Process Management</div></div>

  <div class="abs course" style="left:102px;top:2277px"><div class="course-photo tone-safety" role="img" aria-label="Worker in hard hat and safety vest"></div><div class="course-name">Workplace Safety</div></div>
  <div class="abs course" style="left:355px;top:2277px"><div class="course-photo tone-sales" role="img" aria-label="Presenter at a whiteboard in a meeting"></div><div class="course-name">Sales Training</div></div>
  <div class="abs course" style="left:608px;top:2277px"><div class="course-photo tone-lead" role="img" aria-label="Business team standing together"></div><div class="course-name">Leadership</div></div>
  <div class="abs course" style="left:860px;top:2277px"><div class="course-photo tone-process" role="img" aria-label="Colleagues reviewing work at a computer"></div><div class="course-name">Process Management</div></div>

  <div class="abs btn-outline view-all">View All Courses</div>
</section>

<section>
  <div class="abs testimonials"></div>
  <h2 class="abs center testimonials-title">TESTIMONIALS</h2>

  <div class="abs avatar" style="left:102px;top:2832px" role="img" aria-label="Portrait of a student"></div>
  <div class="abs person" style="left:102px;top:2942px">James Porter</div>
  <div class="abs" style="left:220px;top:2850px">
    <div class="quote-head">Lorem ipsum dolor sit</div>
    <div class="quote-body">Lorem ipsum dolor sit amet, consectetur adipisicing elit, sed do eiusmod tempor incididunt ut labore et dolore magna aliqua.</div>
  </div>

  <div class="abs avatar" style="left:627px;top:2832px" role="img" aria-label="Portrait of a student"></div>
  <div class="abs person" style="left:627px;top:2942px">James Porter</div>
  <div class="abs" style="left:746px;top:2850px">
    <div class="quote-head">Lorem ipsum dolor sit</div>
    <div class="quote-body">Lorem ipsum dolor sit amet, consectetur adipisicing elit, sed do eiusmod tempor incididunt ut labore et dolore magna aliqua.</div>
  </div>
</section>

<section>
  <div class="abs newsletter"></div>
  <h2 class="abs newsletter-title">SUBSCRIBE TO OUR NEWSLETTER</h2>
  <div class="abs email">Email Address</div>
  <div class="abs submit">Submit</div>
</section>

<footer>
  <div class="abs site-footer"></div>
  <p class="abs copyright">© 2016. All rights Reserved.</p>
  <div class="abs socials" aria-label="Social links"><span></span><span></span><span></span><span></span><span></span><span></span></div>
</footer>

</body>
</html>
```